401K Retirement Plan Consultant

Professional & clean lines - not overly busy. We offer two services - 401k administration and HSA administration. Based on the outskirts of Charlotte NC. Communicate the services we offer along with the financial institutions that we work with. Mixture of icons and people pictures.

Current website - tzm401k.com,
It is presently very amateurish.

```html
<!DOCTYPE html>
<html lang="en">
<head>
<meta charset="utf-8">
<title>TZM401k – Homepage</title>
<link href="https://fonts.googleapis.com/css2?family=Figtree:wght@400;500;600;700;800&display=swap" rel="stylesheet">
<style>
:root{
  --backdrop:#b9c5da;
  --blue:#0b57d9;
  --navy:#1c1a4b;
  --ink:#17193f;
  --text:#4d5066;
  --muted:#7d8196;
  --hero:#d9ecf8;
  --why:#d7e3f6;
  --footer:#0c1436;
  --white:#ffffff;
}
*{box-sizing:border-box;margin:0;padding:0}
html,body{width:1140px;height:1200px;overflow:hidden;background:var(--backdrop)}
body{font-family:"Figtree",sans-serif;color:var(--ink)}
.board{position:relative;width:1876px;height:1975px;transform:scale(.6077);transform-origin:0 0;background:var(--backdrop)}
.page{position:absolute;width:790px;overflow:hidden;background:var(--white)}
.page--top{left:124px;top:175px;height:1800px;border-radius:12px 12px 0 0}
.page--bottom{left:963px;top:0;height:1760px;border-radius:0 0 12px 12px}
.sheet{position:absolute;left:0;width:790px;height:2320px}
.page--top .sheet{top:0}
.page--bottom .sheet{top:-560px}
.abs{position:absolute}
.brand{font-weight:800;font-size:19px;color:var(--navy);letter-spacing:-.3px}

/* header */
.site-header{top:0;left:0;width:790px;height:43px;background:var(--white)}
.site-header .brand{position:absolute;left:63px;top:9px}
.nav{position:absolute;left:295px;top:17px;display:flex;gap:29px;font-size:7px;font-weight:600}
.nav a{color:var(--ink);text-decoration:none}
.nav a.active{color:var(--blue)}
.btn{display:inline-flex;align-items:center;justify-content:center;border-radius:5px;font-size:7.5px;font-weight:600;height:31px}
.btn--primary{background:var(--blue);color:var(--white)}
.btn--ghost{background:var(--white);color:var(--blue);box-shadow:0 3px 10px rgba(40,60,120,.15)}
.site-header .btn{position:absolute;left:649px;top:10px;width:76px;height:23px}

/* hero */
.hero{top:43px;left:0;width:790px;height:345px;background:var(--hero)}
.hero h1{position:absolute;left:75px;top:82px;font-size:25px;line-height:32px;font-weight:800;color:var(--navy)}
.hero p{position:absolute;left:75px;top:164px;width:240px;font-size:8px;line-height:13px;color:var(--text)}
.hero p b{color:var(--ink)}
.actions{display:flex;align-items:center;gap:10px}
.actions .or{font-size:7px;color:var(--ink);margin:0 2px}
.hero .actions{position:absolute;left:75px;top:229px}
.hero .btn--primary{width:82px}
.hero .btn--ghost{width:116px}
.photo-frame{position:absolute;left:395px;top:50px;width:330px;height:250px;border-radius:16px;background:rgba(255,255,255,.7);transform:rotate(2.5deg);box-shadow:0 8px 24px rgba(40,60,120,.18)}
.photo{position:absolute;left:6px;top:6px;right:6px;bottom:6px;border-radius:12px;background:linear-gradient(150deg,#c9c2b8 0%,#b7a898 40%,#6f6a58 75%,#2e4a3e 100%)}
.tile{position:absolute;width:38px;height:38px;border-radius:9px;display:flex;align-items:center;justify-content:center}
.tile--blue{background:var(--blue);left:418px;top:44px;transform:rotate(12deg)}
.tile--white{background:var(--white);left:622px;top:60px;transform:rotate(-14deg);box-shadow:0 4px 12px rgba(40,60,120,.2)}
.quote{position:absolute;left:423px;top:247px;width:202px;height:52px;background:var(--white);border-radius:10px;box-shadow:0 4px 14px rgba(40,60,120,.2)}
.quote .pause{position:absolute;left:-6px;top:-8px;width:24px;height:24px;border-radius:6px;background:var(--navy);display:flex;align-items:center;justify-content:center}
.quote p{position:absolute;left:27px;top:12px;font-size:8px;line-height:13px;font-style:italic;color:var(--ink);font-weight:500}
.dot{position:absolute;border-radius:50%}

/* intro */
.intro{top:430px;left:0;width:790px;text-align:center}
.intro h2{font-size:22px;font-weight:800;color:var(--navy)}
.intro p{margin:14px auto 0;width:510px;font-size:11px;line-height:20px;color:var(--ink)}

.features{top:585px;left:0;width:790px;display:flex;justify-content:center}
.feature{width:172px;text-align:center}
.feature .box{width:50px;height:50px;margin:0 auto;background:var(--white);border-radius:10px;box-shadow:0 4px 14px rgba(40,60,120,.12);display:flex;align-items:center;justify-content:center}
.feature span{display:block;margin-top:17px;font-size:8px;line-height:11px;font-weight:700;color:var(--ink)}

.note{top:722px;left:0;width:790px;text-align:center;font-size:8px;line-height:13px;color:var(--text)}

/* cta */
.cta{top:828px;left:87px;width:614px;height:182px;background:var(--navy);border-radius:20px}
.cta p{position:absolute;left:49px;top:41px;font-size:12px;line-height:21px;color:var(--white);font-weight:500}
.cta .actions{position:absolute;left:49px;top:104px}
.cta .btn--primary{width:82px}
.cta .btn--ghost{width:118px}
.cta .or{color:#c7c9e0}
.cta-portrait{position:absolute;left:400px;top:-40px;width:190px;height:222px;border-radius:90px 90px 0 0;background:linear-gradient(180deg,#3a2b22 0%,#7a6553 35%,#8c7a66 70%,#5e4c3d 100%)}

/* services */
.section-title{left:0;width:790px;text-align:center;font-size:16px;font-weight:700;color:var(--navy)}
.section-sub{left:0;width:790px;text-align:center;font-size:8px;line-height:13px;color:var(--text)}
.service{position:absolute;display:flex;align-items:flex-start;gap:12px}
.service .ico{width:38px;height:38px;border-radius:9px;background:var(--blue);box-shadow:0 6px 14px rgba(11,87,217,.3);display:flex;align-items:center;justify-content:center;flex:none}
.service b{display:block;font-size:9.5px;font-weight:700;color:var(--ink);margin-top:2px}
.service small{display:block;font-size:7.5px;line-height:10px;color:var(--muted);margin-top:3px}

/* why */
.why{top:1370px;left:52px;width:686px;height:430px;background:var(--why);border-radius:22px}
.why h2{position:absolute;top:40px;left:0;width:686px;text-align:center;font-size:16px;font-weight:700;color:var(--navy)}
.why > p{position:absolute;top:70px;left:0;width:686px;text-align:center;font-size:8px;line-height:14px;color:var(--text)}
.reason{position:absolute;width:260px}
.reason .box{position:absolute;left:0;top:-6px;width:44px;height:44px;background:var(--white);border-radius:10px;box-shadow:0 4px 12px rgba(40,60,120,.1);display:flex;align-items:center;justify-content:center}
.reason .box i{width:20px;height:20px;border-radius:5px;background:var(--blue);display:flex;align-items:center;justify-content:center}
.reason b{position:absolute;left:58px;top:0;font-size:9px;font-weight:700;color:var(--ink);white-space:nowrap}
.reason small{position:absolute;left:58px;top:15px;width:200px;font-size:7px;line-height:11.5px;color:var(--muted)}

/* partners */
.partners{top:1935px;left:60px;width:670px;display:flex;justify-content:space-between;align-items:center}
.partners span{font-size:14px;font-weight:700;color:#3d4160}

/* footer */
.site-footer{top:2023px;left:0;width:790px;height:297px;background:var(--footer);color:var(--white)}
.site-footer .brand{position:absolute;left:90px;top:50px;color:var(--white)}
.site-footer .about{position:absolute;left:90px;top:90px;width:255px;font-size:7px;line-height:13.5px;color:#aeb4cf}
.label{position:absolute;font-size:5.5px;letter-spacing:1px;font-weight:600;color:#9aa1c0}
.socials{position:absolute;left:90px;top:175px;display:flex;gap:16px;font-size:7px;font-weight:600;color:var(--white)}
.links{position:absolute;left:416px;top:76px;list-style:none;font-size:6.5px;font-weight:600;line-height:20.6px}
.contact{position:absolute;left:525px;display:flex;gap:13px;align-items:flex-start}
.contact .ico{width:28px;height:28px;border-radius:7px;background:var(--white);display:flex;align-items:center;justify-content:center;flex:none}
.contact small{display:block;font-size:6px;color:#aeb4cf;margin-top:2px}
.contact b{display:block;font-size:8px;font-weight:600;line-height:12px;margin-top:3px}
.rule{position:absolute;left:88px;top:245px;width:614px;height:1px;background:#27305a}
.legal{position:absolute;top:263px;font-size:6px;color:#c7ccdf}
</style>
</head>
<body>
<div class="board">

  <!-- upper half of the homepage -->
  <div class="page page--top">
    <div class="sheet">
      <header class="site-header abs">
        <span class="brand">TZM401k</span>
        <nav class="nav"><a class="active" href="#">Home</a><a href="#">Services</a><a href="#">About Us</a><a href="#">Contact Us</a></nav>
        <span class="btn btn--primary">Start Now</span>
      </header>

      <section class="hero abs">
        <h1>Prepare Everything<br>to Live Calmly</h1>
        <p>Setting up an employee retirement plan can be a smart way to provide for one of your key assets<br><b>– your people.</b></p>
        <div class="actions"><span class="btn btn--primary">Get a Quote</span><span class="or">or</span><span class="btn btn--ghost">Arrange Consultation</span></div>
        <div class="photo-frame"><div class="photo" role="img" aria-label="Photo of a smiling retired couple sitting together at home"></div></div>
        <span class="tile tile--blue"><svg width="16" height="16" viewBox="0 0 16 16"><path d="M8 1l6 2.5v4C14 11 11.5 14 8 15 4.5 14 2 11 2 7.5v-4z" fill="#fff"/><path d="M5.5 8l2 2 3-4" stroke="#0b57d9" stroke-width="1.6" fill="none"/></svg></span>
        <span class="tile tile--white"><svg width="16" height="16" viewBox="0 0 16 16"><circle cx="8" cy="8" r="6.5" fill="#0b57d9"/><path d="M5 8.2l2 2 4-4" stroke="#fff" stroke-width="1.6" fill="none"/></svg></span>
        <span class="dot" style="left:716px;top:222px;width:11px;height:11px;background:#7fb5e6"></span>
        <span class="dot" style="left:716px;top:50px;width:7px;height:7px;background:var(--blue)"></span>
        <span class="dot" style="left:343px;top:180px;width:5px;height:5px;background:#4a3fb5"></span>
        <div class="quote">
          <span class="pause"><svg width="10" height="10" viewBox="0 0 10 10"><rect x="2" y="1" width="2" height="8" fill="#fff"/><rect x="6" y="1" width="2" height="8" fill="#fff"/></svg></span>
          <p>After Using TZM401k the burden of<br>my mind feels very less.</p>
        </div>
      </section>

      <section class="intro abs">
        <h2>401k</h2>
        <p>TZM401k has been providing employee benefit services since 1987.&nbsp; Our plans gives you the flexibility to customize a retirement plan that meets the specific needs of your company and the employees. Our IRS approved 401(k) plans are:</p>
      </section>

      <div class="features abs">
        <div class="feature"><div class="box"><svg width="18" height="18" viewBox="0 0 18 18"><rect x="3" y="3" width="12" height="12" rx="4" fill="#4a5fa0"/><circle cx="8" cy="8" r="3" fill="#c9d4ef"/></svg></div><span>Designed especially for<br>smaller plans</span></div>
        <div class="feature"><div class="box"><svg width="18" height="18" viewBox="0 0 18 18"><rect x="3" y="3" width="12" height="13" rx="2.5" fill="#4a5fa0"/><rect x="6" y="1.5" width="6" height="3" rx="1" fill="#4a5fa0"/><path d="M6 10l2 2 4-4" stroke="#fff" stroke-width="1.5" fill="none"/></svg></div><span>Simple to operate and<br>maintain</span></div>
        <div class="feature"><div class="box"><svg width="18" height="18" viewBox="0 0 18 18"><rect x="3" y="5" width="12" height="11" rx="2.5" fill="#4a5fa0"/><path d="M6.5 5V3.5h5V5" stroke="#4a5fa0" stroke-width="1.5" fill="none"/><text x="9" y="13.5" font-size="7" font-weight="700" fill="#fff" text-anchor="middle" font-family="Figtree,sans-serif">$</text></svg></div><span>Low-cost recordkeeping<br>and investments</span></div>
      </div>

      <p class="note abs">Most people realize that, we all have to accept more responsibility for saving for our own retirement.<br>It’s widely accepted that Social Security is only meant to provide a modest percentage of your<br>retirement income—so Social Security alone will not be enough.</p>

      <section class="cta abs">
        <div class="cta-portrait" role="img" aria-label="Photo of a smiling consultant holding a folder"></div>
        <p>Contact us today to request a custom fee comparison or<br>a quote for a startup plan.&nbsp; It’s quick and easy.</p>
        <div class="actions"><span class="btn btn--primary">Get a Quote</span><span class="or">or</span><span class="btn btn--ghost">Arrange Consultation</span></div>
      </section>

      <h2 class="section-title abs" style="top:1064px">Our Other Services</h2>
      <p class="section-sub abs" style="top:1097px">While you can use the funds in an 401k at any time to pay for qualified medical expenses,<br>you may contribute to our other programs too.</p>
      <div class="service" style="left:150px;top:1168px"><span class="ico"><svg width="14" height="14" viewBox="0 0 14 14"><path d="M7 1l5 2v3.5C12 10 9.8 12.3 7 13 4.2 12.3 2 10 2 6.5V3z" fill="#fff"/><path d="M7 4.5v5M4.5 7h5" stroke="#0b57d9" stroke-width="1.5"/></svg></span><div><b>HSA</b><small>Health Savings<br>Account</small></div></div>
      <div class="service" style="left:337px;top:1168px"><span class="ico"><svg width="14" height="14" viewBox="0 0 14 14"><rect x="1.5" y="3" width="11" height="8" rx="1.5" fill="#fff"/><rect x="1.5" y="5" width="11" height="1.5" fill="#0b57d9"/></svg></span><div><b>FSA</b><small>Flexible Spending<br>Account</small></div></div>
      <div class="service" style="left:525px;top:1168px"><span class="ico"><svg width="14" height="14" viewBox="0 0 14 14"><rect x="1.5" y="2.5" width="11" height="9" rx="2" fill="#fff"/><path d="M3 7h2l1-2 2 4 1-2h2" stroke="#0b57d9" stroke-width="1.2" fill="none"/></svg></span><div><b>HSA</b><small>Health Reimbursement<br>Account</small></div></div>
      <div class="service" style="left:244px;top:1246px"><span class="ico"><svg width="14" height="14" viewBox="0 0 14 14"><rect x="2" y="3" width="10" height="9" rx="1.5" fill="#fff"/><rect x="4" y="1.5" width="1.5" height="3" fill="#fff"/><rect x="8.5" y="1.5" width="1.5" height="3" fill="#fff"/><rect x="4" y="7" width="6" height="1.5" fill="#0b57d9"/></svg></span><div><b>COBRA</b><small>Health Insurance<br>Continuation</small></div></div>
      <div class="service" style="left:431px;top:1246px"><span class="ico"><svg width="14" height="14" viewBox="0 0 14 14"><rect x="2" y="3" width="10" height="9" rx="1.5" fill="#fff"/><rect x="4" y="1.5" width="1.5" height="3" fill="#fff"/><rect x="8.5" y="1.5" width="1.5" height="3" fill="#fff"/><rect x="4" y="7" width="6" height="1.5" fill="#0b57d9"/></svg></span><div><b>Dependent Care</b><small>Dependent Care</small></div></div>

      <section class="why abs">
        <h2>Why TZM401k is Better</h2>
        <p>We provide a full service for our clients, this is placeholder text commonly used in the graphic, print, and<br>publishing industries for previewing layouts to fill with your own contents.</p>
        <div class="reason" style="left:70px;top:143px"><span class="box"><i><svg width="10" height="10" viewBox="0 0 10 10"><path d="M4 3L2 5l2 2M6 3l2 2-2 2" stroke="#fff" stroke-width="1.2" fill="none"/></svg></i></span><b>Open Architecture Platform</b><small>Offering participants a wide range of investment choices instead of a fixed set of funds.</small></div>
        <div class="reason" style="left:371px;top:143px"><span class="box"><i></i></span><b>Plan Design &amp; Document Services</b><small>Preparation of the Volume Submitter document, adoption agreement, and all required forms and notices.</small></div>
        <div class="reason" style="left:70px;top:210px"><span class="box"><i></i></span><b>Employee Education</b><small>We provides participants with group educational meetings, helping them prepare for retirement.</small></div>
        <div class="reason" style="left:371px;top:210px"><span class="box"><svg width="18" height="18" viewBox="0 0 18 18"><circle cx="5" cy="5" r="3.5" fill="#0b57d9"/><circle cx="13" cy="5" r="3.5" fill="#0b57d9"/><circle cx="5" cy="13" r="3.5" fill="#0b57d9"/><circle cx="13" cy="13" r="3.5" fill="#0b57d9"/></svg></span><b>FSA, HRA and Dependent Care</b><small>These plans are pre-approved by the Internal Revenue Service.</small></div>
        <div class="reason" style="left:70px;top:277px"><span class="box"><i></i></span><b>HSA Administration</b><small>We offer an HSA Debit Card for easy access to your funds, with transactions limited to your current balance.</small></div>
        <div class="reason" style="left:371px;top:277px"><span class="box"><i></i></span><b>Employer Allocation Preparation</b><small>Calculation of Employer Matching and/or Profit Sharing Contribution using various allocation methods.</small></div>
        <div class="reason" style="left:70px;top:344px"><span class="box"><i></i></span><b>IRS 5500 &amp; 1099-R’s</b><small>ERISA Form 5500 is prepared annually, along with the 1099-R, which reports plan withdrawals.</small></div>
        <div class="reason" style="left:371px;top:340px"><span class="box"><i></i></span><b>Non-Discrimination Testing</b><small>Ensure that highly compensated employees do not disproportionately benefit from tax savings compared to lower-paid employees.</small></div>
      </section>
    </div>
  </div>

  <!-- lower half of the homepage -->
  <div class="page page--bottom">
    <div class="sheet">
      <div class="features abs">
        <div class="feature"><div class="box"><svg width="18" height="18" viewBox="0 0 18 18"><rect x="3" y="3" width="12" height="12" rx="4" fill="#4a5fa0"/><circle cx="8" cy="8" r="3" fill="#c9d4ef"/></svg></div><span>Designed especially for<br>smaller plans</span></div>
        <div class="feature"><div class="box"><svg width="18" height="18" viewBox="0 0 18 18"><rect x="3" y="3" width="12" height="13" rx="2.5" fill="#4a5fa0"/><rect x="6" y="1.5" width="6" height="3" rx="1" fill="#4a5fa0"/><path d="M6 10l2 2 4-4" stroke="#fff" stroke-width="1.5" fill="none"/></svg></div><span>Simple to operate and<br>maintain</span></div>
        <div class="feature"><div class="box"><svg width="18" height="18" viewBox="0 0 18 18"><rect x="3" y="5" width="12" height="11" rx="2.5" fill="#4a5fa0"/><path d="M6.5 5V3.5h5V5" stroke="#4a5fa0" stroke-width="1.5" fill="none"/><text x="9" y="13.5" font-size="7" font-weight="700" fill="#fff" text-anchor="middle" font-family="Figtree,sans-serif">$</text></svg></div><span>Low-cost recordkeeping<br>and investments</span></div>
      </div>

      <p class="note abs">Most people realize that, we all have to accept more responsibility for saving for our own retirement.<br>It’s widely accepted that Social Security is only meant to provide a modest percentage of your<br>retirement income—so Social Security alone will not be enough.</p>

      <section class="cta abs">
        <div class="cta-portrait" role="img" aria-label="Photo of a smiling consultant holding a folder"></div>
        <p>Contact us today to request a custom fee comparison or<br>a quote for a startup plan.&nbsp; It’s quick and easy.</p>
        <div class="actions"><span class="btn btn--primary">Get a Quote</span><span class="or">or</span><span class="btn btn--ghost">Arrange Consultation</span></div>
      </section>

      <h2 class="section-title abs" style="top:1064px">Our Other Services</h2>
      <p class="section-sub abs" style="top:1097px">While you can use the funds in an 401k at any time to pay for qualified medical expenses,<br>you may contribute to our other programs too.</p>
      <div class="service" style="left:150px;top:1168px"><span class="ico"><svg width="14" height="14" viewBox="0 0 14 14"><path d="M7 1l5 2v3.5C12 10 9.8 12.3 7 13 4.2 12.3 2 10 2 6.5V3z" fill="#fff"/><path d="M7 4.5v5M4.5 7h5" stroke="#0b57d9" stroke-width="1.5"/></svg></span><div><b>HSA</b><small>Health Savings<br>Account</small></div></div>
      <div class="service" style="left:337px;top:1168px"><span class="ico"><svg width="14" height="14" viewBox="0 0 14 14"><rect x="1.5" y="3" width="11" height="8" rx="1.5" fill="#fff"/><rect x="1.5" y="5" width="11" height="1.5" fill="#0b57d9"/></svg></span><div><b>FSA</b><small>Flexible Spending<br>Account</small></div></div>
      <div class="service" style="left:525px;top:1168px"><span class="ico"><svg width="14" height="14" viewBox="0 0 14 14"><rect x="1.5" y="2.5" width="11" height="9" rx="2" fill="#fff"/><path d="M3 7h2l1-2 2 4 1-2h2" stroke="#0b57d9" stroke-width="1.2" fill="none"/></svg></span><div><b>HSA</b><small>Health Reimbursement<br>Account</small></div></div>
      <div class="service" style="left:244px;top:1246px"><span class="ico"><svg width="14" height="14" viewBox="0 0 14 14"><rect x="2" y="3" width="10" height="9" rx="1.5" fill="#fff"/><rect x="4" y="1.5" width="1.5" height="3" fill="#fff"/><rect x="8.5" y="1.5" width="1.5" height="3" fill="#fff"/><rect x="4" y="7" width="6" height="1.5" fill="#0b57d9"/></svg></span><div><b>COBRA</b><small>Health Insurance<br>Continuation</small></div></div>
      <div class="service" style="left:431px;top:1246px"><span class="ico"><svg width="14" height="14" viewBox="0 0 14 14"><rect x="2" y="3" width="10" height="9" rx="1.5" fill="#fff"/><rect x="4" y="1.5" width="1.5" height="3" fill="#fff"/><rect x="8.5" y="1.5" width="1.5" height="3" fill="#fff"/><rect x="4" y="7" width="6" height="1.5" fill="#0b57d9"/></svg></span><div><b>Dependent Care</b><small>Dependent Care</small></div></div>

      <section class="why abs">
        <h2>Why TZM401k is Better</h2>
        <p>We provide a full service for our clients, this is placeholder text commonly used in the graphic, print, and<br>publishing industries for previewing layouts to fill with your own contents.</p>
        <div class="reason" style="left:70px;top:143px"><span class="box"><i><svg width="10" height="10" viewBox="0 0 10 10"><path d="M4 3L2 5l2 2M6 3l2 2-2 2" stroke="#fff" stroke-width="1.2" fill="none"/></svg></i></span><b>Open Architecture Platform</b><small>Offering participants a wide range of investment choices instead of a fixed set of funds.</small></div>
        <div class="reason" style="left:371px;top:143px"><span class="box"><i></i></span><b>Plan Design &amp; Document Services</b><small>Preparation of the Volume Submitter document, adoption agreement, and all required forms and notices.</small></div>
        <div class="reason" style="left:70px;top:210px"><span class="box"><i></i></span><b>Employee Education</b><small>We provides participants with group educational meetings, helping them prepare for retirement.</small></div>
        <div class="reason" style="left:371px;top:210px"><span class="box"><svg width="18" height="18" viewBox="0 0 18 18"><circle cx="5" cy="5" r="3.5" fill="#0b57d9"/><circle cx="13" cy="5" r="3.5" fill="#0b57d9"/><circle cx="5" cy="13" r="3.5" fill="#0b57d9"/><circle cx="13" cy="13" r="3.5" fill="#0b57d9"/></svg></span><b>FSA, HRA and Dependent Care</b><small>These plans are pre-approved by the Internal Revenue Service.</small></div>
        <div class="reason" style="left:70px;top:277px"><span class="box"><i></i></span><b>HSA Administration</b><small>We offer an HSA Debit Card for easy access to your funds, with transactions limited to your current balance.</small></div>
        <div class="reason" style="left:371px;top:277px"><span class="box"><i></i></span><b>Employer Allocation Preparation</b><small>Calculation of Employer Matching and/or Profit Sharing Contribution using various allocation methods.</small></div>
        <div class="reason" style="left:70px;top:344px"><span class="box"><i></i></span><b>IRS 5500 &amp; 1099-R’s</b><small>ERISA Form 5500 is prepared annually, along with the 1099-R, which reports plan withdrawals.</small></div>
        <div class="reason" style="left:371px;top:340px"><span class="box"><i></i></span><b>Non-Discrimination Testing</b><small>Ensure that highly compensated employees do not disproportionately benefit from tax savings compared to lower-paid employees.</small></div>
      </section>

      <h2 class="section-title abs" style="top:1856px">Our Partners</h2>
      <div class="partners abs">
        <span>Fernwell</span><span>Crestline Funds</span><span>Veyra</span><span>Ampora</span><span>Alvaro</span><span>Westbrook Klein</span>
      </div>

      <footer class="site-footer abs">
        <span class="brand">TZM401k</span>
        <p class="about">TZM401k has been providing employee benefit services since 1987 that gives you the flexibility to customize a retirement plan that meets the specific needs of your company and the employees.</p>
        <span class="label" style="left:90px;top:156px">FOLLOW US ON</span>
        <div class="socials"><span>Kin</span><span>Peep</span><span>Lens</span></div>
        <span class="label" style="left:416px;top:51px">QUICK LINKS</span>
        <ul class="links"><li>About Us</li><li>Services</li><li>Feature</li><li>Blog</li><li>FAQs</li></ul>
        <span class="label" style="left:525px;top:51px">CONTACT &amp; INFORMATION</span>
        <div class="contact" style="top:77px"><span class="ico"><svg width="12" height="12" viewBox="0 0 12 12"><path d="M3 1.5l2 2.5-1.2 1.2a6 6 0 003 3L8 7l2.5 2-1 1.5C5 10.5 1.5 7 1.5 2.5z" fill="#0b57d9"/></svg></span><div><small>Phone Number</small><b>1 704 555 0148</b></div></div>
        <div class="contact" style="top:125px"><span class="ico"><svg width="12" height="12" viewBox="0 0 12 12"><circle cx="6" cy="6" r="5" fill="#0b57d9"/><path d="M6 3.5V6l1.8 1.2" stroke="#fff" stroke-width="1.1" fill="none"/></svg></span><div><small>Open Hour</small><b>09:00 AM - 18:00 PM</b></div></div>
        <div class="contact" style="top:172px"><span class="ico"><svg width="12" height="12" viewBox="0 0 12 12"><path d="M6 11.5S2 7.5 2 4.8a4 4 0 018 0C10 7.5 6 11.5 6 11.5z" fill="#0b57d9"/><circle cx="6" cy="4.8" r="1.5" fill="#fff"/></svg></span><div><small>Headquarter Address</small><b>1280 Harbor Ridge Rd Suite 110<br>Lakemont SC 29700</b></div></div>
        <div class="rule"></div>
        <span class="legal" style="left:90px">©TZM401k by Lanternway. All Right Reserved</span>
        <span class="legal" style="left:579px">Terms of Use</span>
        <span class="legal" style="left:656px">Privacy Policy</span>
      </footer>
    </div>
  </div>

</div>
</body>
</html>
```